Logo and 1 page Flyer for Meridian Fund

We need a logo and a 1 single page flyer for an Investment Fund we'll distribute worldwide. It'a Meridian Fund that will give a return also to the poorest people in the world. Details inside. We give just an idea (based on a previous flyer we had here) with the attached draft. Anyone can figure out how to make its own. NOTE: LQV is our company's logo.

Target Market(s)

Investors

Industry/Entity Type

Finance And Accounting

Logo Text

KOLB Kindred Open Bloom Fund

Font styles to use
Serif

Colors
00a990

Requirements
Must have
• A logo you choose which should be:
• - Elegant
• - Innovative
• - Crypto evoking (Company launching is a cripto company)
• - Hi tech
Nice to have
• We have sent you all materials to be able to understand:
• 1. A draft of how we would like the texts to come out. Don't use this (we're already using with other texts), ,but see the evidence of Logo, Slogan, and the 3 main characteristics. Also notice very well that is very elegant. Use a real light on color, make it as shining as you can. It must be a sort of shining green, expressing Hope, Beauty, Well being
• 2. The logo for LQV that is the company launching the project. In draft you see on low left. You can put wherever you feel right
• 3. All texts are on draft to be seen, and on word to be used. You can choose font and dimensions as you prefer
• 4. We've given you logo we have for PIRO. If you feel, you can use in the line where we talk about it or place somewhere. Not mandatory
Should not have
• Funny things; too commercial style; unprofessional aspect

```html
<!DOCTYPE html>
<html lang="en">
<head>
<meta charset="utf-8">
<title>KOLB Flyer – Front and Back</title>
<link href="https://fonts.googleapis.com/css2?family=Playfair+Display:wght@700;900&family=Lora:wght@400;600;700&display=swap" rel="stylesheet">
<style>
  :root{
    --stage:#3a3a3c;
    --label:#8a8a8c;
    --green-deep:#006e5d;
    --green:#00a990;
    --green-bright:#2fd1b2;
    --green-glow:#8ff0d8;
    --green-pale:#cdf3ea;
    --ink-green:#00876f;
    --text:#2b2b2b;
    --white:#ffffff;
  }
  *{box-sizing:border-box;margin:0;padding:0}
  html,body{width:1200px;height:910px;overflow:hidden;background:var(--stage)}
  body{position:relative;font-family:"Lora",Georgia,serif}

  .side-label{position:absolute;top:68px;font-size:38px;font-weight:400;color:var(--label);text-align:center;width:499px}
  .side-label--front{left:84px}
  .side-label--back{left:616px}

  .flyer{position:absolute;top:135px;width:499px;height:705px;overflow:hidden}
  .flyer--front{left:84px;background:var(--white)}
  .flyer--back{left:616px}
  .flyer svg.backdrop{position:absolute;inset:0}

  /* Front */
  .brand{position:absolute;left:0;top:0;width:212px;text-align:center;color:var(--white)}
  .brand__mark{position:absolute;left:76px;top:102px;width:60px;height:60px;border:3px solid var(--white);border-radius:50%}
  .brand__name{position:absolute;left:0;width:212px;top:182px;font-family:"Playfair Display",Georgia,serif;font-size:56px;font-weight:900;letter-spacing:1px;line-height:1}
  .brand__tagline{position:absolute;left:0;width:212px;top:246px;font-size:10px;font-weight:700;letter-spacing:.2px}

  .headline{position:absolute;left:0;width:499px;top:396px;text-align:center;color:var(--ink-green);font-family:"Playfair Display",Georgia,serif;font-weight:900;font-size:39px;line-height:41px}
  .intro{position:absolute;left:56px;width:387px;top:490px;text-align:center;color:var(--text);font-size:11px;line-height:13px}

  .features{position:absolute;left:0;top:547px;width:499px;height:70px}
  .feature{position:absolute;top:0;width:156px;text-align:center}
  .feature--return{left:16px}
  .feature--anyone{left:187px}
  .feature--heart{left:343px}
  .feature__title{color:var(--ink-green);font-family:"Playfair Display",Georgia,serif;font-weight:700;font-size:13.5px;line-height:16px;margin-top:4px}
  .feature__text{color:var(--text);font-size:9.5px;line-height:12.5px;margin-top:8px}
  .divider{position:absolute;top:0;width:1.5px;height:68px;background:#555}
  .divider--one{left:184px}
  .divider--two{left:344px}

  .web{position:absolute;left:0;width:499px;top:664px;text-align:center;font-size:17px;font-weight:700;line-height:28px}
  .web--front{color:var(--white)}
  .web--back{color:var(--ink-green)}

  /* Back */
  .partner{position:absolute;left:104px;top:372px;height:100px;width:340px}
  .partner__mark{position:absolute;left:0;top:0;width:100px;height:100px;border-radius:50%;background:var(--white)}
  .partner__name{position:absolute;left:112px;top:-4px;font-family:"Playfair Display",Georgia,serif;font-weight:700;font-size:88px;line-height:100px;color:var(--white)}
  .partner__tagline{position:absolute;left:114px;top:92px;font-weight:600;font-size:14px;letter-spacing:1.5px;color:var(--white)}
</style>
</head>
<body>

<div class="side-label side-label--front">Front</div>
<div class="side-label side-label--back">Back</div>

<!-- Front side -->
<section class="flyer flyer--front">
  <svg class="backdrop" width="499" height="705" viewBox="0 0 499 705">
    <defs>
      <linearGradient id="frontGreen" x1="0" y1="0" x2="1" y2="1">
        <stop offset="0" stop-color="#007d68"/>
        <stop offset=".5" stop-color="#00b89b"/>
        <stop offset="1" stop-color="#008f78"/>
      </linearGradient>
      <radialGradient id="techGlow" cx=".62" cy=".38" r=".6">
        <stop offset="0" stop-color="#e9fff8"/>
        <stop offset=".15" stop-color="#6ff0d2"/>
        <stop offset=".45" stop-color="#006a5a"/>
        <stop offset="1" stop-color="#021a17"/>
      </radialGradient>
      <linearGradient id="whitePanel" x1="0" y1="0" x2="1" y2="0">
        <stop offset="0" stop-color="#dcf5ef"/>
        <stop offset=".2" stop-color="#ffffff"/>
        <stop offset=".85" stop-color="#ffffff"/>
        <stop offset="1" stop-color="#d4f2ea"/>
      </linearGradient>
    </defs>
    <rect width="499" height="705" fill="url(#frontGreen)"/>
    <polygon points="0,0 44,0 0,36" fill="#5fdcc2"/>
    <polygon points="0,400 120,260 170,340 0,370" fill="#3cd0b3" opacity=".5"/>
    <polygon role="img" aria-label="Glowing hi-tech circuit dial with a bright core" points="120,0 499,0 499,288 420,262 340,262 258,258" fill="url(#techGlow)"/>
    <polygon points="340,262 420,262 499,288 499,300 360,300" fill="#1fbf9f"/>
    <polygon points="255,258 330,262 362,330 296,340" fill="#7fe6cf" opacity=".8"/>
    <polygon points="258,258 285,258 296,340 270,340" fill="#e0f8f2"/>
    <path d="M0,352 Q240,292 499,356 L499,705 L0,705 Z" fill="url(#whitePanel)"/>
    <path d="M176,705 L176,690 Q176,662 206,662 L294,662 Q326,662 326,690 L326,693 L499,693 L499,705 Z" fill="var(--green-deep)"/>
    <rect x="0" y="693" width="499" height="12" fill="var(--green-deep)"/>
    <polygon points="0,705 0,698 70,693 130,693" fill="var(--green-bright)" opacity=".6"/>
  </svg>

  <div class="brand">
    <div class="brand__mark"></div>
    <div class="brand__name">KOLB</div>
    <div class="brand__tagline">Kindred Open Bloom Fund</div>
  </div>

  <h1 class="headline">Raise The Poor<br>Surfing With Us</h1>
  <p class="intro">With KOLB you achieve sound return on your investment. And you help needy ones to obtain real help in their life.</p>

  <div class="features">
    <div class="feature feature--return">
      <h2 class="feature__title">Better RETURN</h2>
      <p class="feature__text">Using PIRO – Precision Intelligent Risk Optimizer. A breakthrough in money management</p>
    </div>
    <span class="divider divider--one"></span>
    <div class="feature feature--anyone">
      <h2 class="feature__title">For ANYONE</h2>
      <p class="feature__text">For those who can invest.<br>And for those Who have no money to survive.</p>
    </div>
    <span class="divider divider--two"></span>
    <div class="feature feature--heart">
      <h2 class="feature__title">Money and HEART</h2>
      <p class="feature__text">To have a return that<br>Warms you and others.</p>
    </div>
  </div>

  <div class="web web--front">www.lqvf.io</div>
</section>

<!-- Back side -->
<section class="flyer flyer--back">
  <svg class="backdrop" width="500" height="705" viewBox="0 0 500 705">
    <defs>
      <linearGradient id="backGreen" x1="0" y1="0" x2=".6" y2="1">
        <stop offset="0" stop-color="#007a66"/>
        <stop offset=".5" stop-color="#12c2a2"/>
        <stop offset="1" stop-color="#00937b"/>
      </linearGradient>
    </defs>
    <rect width="500" height="705" fill="url(#backGreen)"/>
    <polygon points="0,0 44,0 0,30" fill="#5fdcc2"/>
    <circle role="img" aria-label="Large pale disc used as a soft background accent" cx="364" cy="125" r="201" fill="var(--green-pale)" opacity=".8"/>
    <path d="M158,705 L158,690 Q158,662 190,662 L310,662 Q342,662 342,690 L342,693 L500,693 L500,705 Z" fill="var(--white)"/>
    <rect x="0" y="693" width="500" height="12" fill="var(--white)"/>
  </svg>

  <div class="partner">
    <span class="partner__mark"></span>
    <span class="partner__name">LQV</span>
    <span class="partner__tagline">LedgerQuantVest</span>
  </div>

  <div class="web web--back">www.lqvf.io</div>
</section>

</body>
</html>
```